Business card and stationary design
Lindora Development
Business card and stationary design -
Creative Brief
Simple
Marike Holzner - van Brugt
MSc, Dipl. Coach & Consultant
Feldrainweg 14 6318 Cham Switzerland
info@lindoradevelopment.ch
www.lindoradevelopment.ch
We're not sure about the font-type, could be the Logo-type or something that's compatible
Personal Coaching Health Coaching Business Coaching Consultancy out of the box, into the outdoors

```html
<!DOCTYPE html>
<html lang="en">
<head>
<meta charset="utf-8">
<title>Lindora Development – Business Card</title>
<link rel="stylesheet" href="https://fonts.googleapis.com/css2?family=PT+Sans:ital,wght@0,700;1,400;1,700&family=Tinos:wght@400&display=swap">
<style>
  :root {
    --page-bg: #e9e6e2;
    --card-bg: #ffffff;
    --band-dark: #1f6fb6;
    --band-light: #6fb6ea;
    --accent-green: #7cb342;
    --name-blue: #1d74c2;
    --title-green: #6f9f2a;
    --body-text: #3a3a3a;
    --icon-blue: #2a6fad;
    --divider: #c9c9c9;
  }
  html, body {
    margin: 0;
    width: 1200px;
    height: 780px;
    overflow: hidden;
    background: var(--page-bg);
  }
  .canvas {
    position: relative;
    width: 1200px;
    height: 780px;
  }
  .card {
    position: absolute;
    left: 100px;
    top: 100px;
    width: 1000px;
    height: 580px;
    background: linear-gradient(180deg, #ffffff 0%, #f3f3f3 100%);
    border-radius: 30px;
    overflow: hidden;
    box-shadow: 0 6px 18px rgba(0,0,0,0.12);
  }
  .card__band {
    position: absolute;
    left: 0; top: 0; bottom: 0;
    width: 52px;
    background: linear-gradient(90deg, var(--band-dark) 0%, var(--band-light) 100%);
  }
  .card__band-line {
    position: absolute;
    left: 56px; top: 0; bottom: 0;
    width: 4px;
    background: var(--accent-green);
  }
  .brand {
    position: absolute;
    left: 80px;
    top: 200px;
    width: 340px;
    display: flex;
    flex-direction: column;
    align-items: center;
    gap: 22px;
  }
  .brand__dot {
    width: 110px;
    height: 110px;
    border-radius: 50%;
    background: var(--name-blue);
  }
  .brand__name {
    font-family: "Tinos", serif;
    font-size: 34px;
    color: var(--name-blue);
    letter-spacing: 1px;
    text-align: center;
    line-height: 1.1;
  }
  .divider {
    position: absolute;
    left: 432px;
    top: 110px;
    width: 2px;
    height: 380px;
    background: var(--divider);
  }
  .details {
    position: absolute;
    left: 452px;
    top: 78px;
    right: 30px;
  }
  .details__name {
    font-family: "PT Sans", sans-serif;
    font-weight: 700;
    font-size: 36px;
    color: var(--name-blue);
    margin: 0;
  }
  .details__title {
    font-family: "PT Sans", sans-serif;
    font-style: italic;
    font-weight: 700;
    font-size: 24px;
    color: var(--title-green);
    margin: 2px 0 30px;
  }
  .details__address {
    font-family: "Tinos", serif;
    font-size: 25px;
    color: var(--body-text);
    line-height: 1.3;
    margin: 0 0 22px;
  }
  .contact {
    list-style: none;
    margin: 0;
    padding: 0;
    font-family: "Tinos", serif;
    font-size: 24px;
    color: var(--body-text);
  }
  .contact__item {
    display: flex;
    align-items: center;
    gap: 14px;
    height: 40px;
  }
  .contact__icon {
    width: 22px;
    height: 22px;
    flex: none;
  }
</style>
</head>
<body>
<div class="canvas">
  <div class="card">
    <div class="card__band"></div>
    <div class="card__band-line"></div>

    <div class="brand">
      <div class="brand__dot"></div>
      <div class="brand__name">Lindora Development</div>
    </div>

    <div class="divider"></div>

    <div class="details">
      <h1 class="details__name">Marike Holzner - van Brugt</h1>
      <p class="details__title">MSc, Dipl. Coach &amp; Consultant</p>
      <p class="details__address">Feldrainweg 14<br>6318 Cham, Switzerland</p>
      <ul class="contact">
        <li class="contact__item">
          <svg class="contact__icon" viewBox="0 0 24 24" aria-hidden="true"><path fill="var(--icon-blue)" d="M6.6 10.8a15.1 15.1 0 0 0 6.6 6.6l2.2-2.2a1 1 0 0 1 1-.25 11.4 11.4 0 0 0 3.6.57 1 1 0 0 1 1 1V20a1 1 0 0 1-1 1A17 17 0 0 1 3 4a1 1 0 0 1 1-1h3.5a1 1 0 0 1 1 1c0 1.25.2 2.45.57 3.6a1 1 0 0 1-.25 1z"/></svg>
          +41 (0)41 702 18 46
        </li>
        <li class="contact__item">
          <svg class="contact__icon" viewBox="0 0 24 24" aria-hidden="true"><rect x="6" y="2" width="12" height="20" rx="2" fill="var(--icon-blue)"/><rect x="8" y="5" width="8" height="12" fill="#fff"/><circle cx="12" cy="19.2" r="1" fill="#fff"/></svg>
          +41 (0)78 315 60 29
        </li>
        <li class="contact__item">
          <svg class="contact__icon" viewBox="0 0 24 24" aria-hidden="true"><circle cx="12" cy="12" r="4" fill="none" stroke="var(--icon-blue)" stroke-width="2.4"/><path d="M16 8v5.5a2.5 2.5 0 0 0 5 0V12a9 9 0 1 0-3.5 7.1" fill="none" stroke="var(--icon-blue)" stroke-width="2.4"/></svg>
          info@lindoradevelopment.ch
        </li>
        <li class="contact__item">
          <svg class="contact__icon" viewBox="0 0 24 24" aria-hidden="true"><circle cx="12" cy="12" r="10" fill="var(--icon-blue)"/><g fill="none" stroke="#fff" stroke-width="1.4"><ellipse cx="12" cy="12" rx="4" ry="10"/><path d="M2 12h20M4 7h16M4 17h16"/></g></svg>
          www.lindoradevelopment.ch
        </li>
      </ul>
    </div>
  </div>
</div>
</body>
</html>
```